Upstart Retirement Planning Firm needs help with business card design

Harborlight Wealth Partners, LLC is looking for help with business card design. We give advice on investments, insurance, and other financial matters related to retirement. There are some required disclosures that we will provide but mostly we are looking for a professional, classy business card that reflects the theme we have chosen. We have a logo that is attached but we would like to add a phrase; "Turning Your Earned Income Into Retirement Income"

Doubled sided only so that we can add the required disclosures (needed for our industry) on the back of the card. We will provide the exact words for this in 1-2 days.

Target Market(s)

Retirees and Pre-retirees. Professionals 50+ years old

Industry/Entity Type

Financial Planning

Contact Information for Business Card

We currently have two people who will need separate cards so we'd like to have a template so that we can add names for new cards in the future.

For the first run, please show the following information.

Neil Osgood, MBA, ChFC®, CLU®
Financial Advisor, Registered Representative
nosgood@harborlightwp.example
Phone: (555) 218-3960
Toll Free Fax: (555) 218-3961

Address is
2876 Meadowbrook Pkwy.
Suite K418
Virginia Beach, VA 23019

Colors
3277b5

Requirements
Must have
• Logo, contact info, small phase to describe business (in description), required legal disclosures on back of the card as follows (in small font)
• Neil Osgood is a registered representative of and offers securities through Brightwater Capital Brokerage Corporation, Member SIPC. Brightwater Capital Brokerage Corporation is a member of the Brightwater Advisory Group which is the marketing name for Brightwater Holding Corporation and its affiliates.
Nice to have
• Rounded edges, raised letters
Should not have
• any colors that aren't in the logo (other than black for font)

```html
<!DOCTYPE html>
<html lang="en">
<head>
<meta charset="utf-8">
<title>Harborlight Wealth Partners — Business Card</title>
<link rel="stylesheet" href="https://fonts.googleapis.com/css2?family=Tinos:wght@400;700&display=swap">
<style>
  :root {
    --brand-blue: #2b55a0;
    --band-grey: #9b9b9b;
    --card-white: #ffffff;
    --ink: #111111;
    --muted-ink: #333333;
    --page: #e6e6e6;
  }
  * { margin: 0; padding: 0; box-sizing: border-box; }
  html, body {
    width: 1189px;
    height: 1200px;
    overflow: hidden;
    background: var(--page);
    font-family: "Tinos", "Times New Roman", serif;
  }
  .card {
    position: absolute;
    left: 140px;
    width: 916px;
    background: var(--card-white);
    overflow: hidden;
  }
  .card--front { top: 45px; height: 524px; }
  .card--back  { top: 628px; height: 522px; }

  .brand {
    position: absolute;
    left: 0;
    width: 100%;
    text-align: center;
  }
  .card--front .brand { top: 92px; }
  .card--back .brand  { top: 196px; }

  .brand__name {
    color: var(--brand-blue);
    font-weight: 700;
    font-size: 36px;
    line-height: 44px;
    letter-spacing: 0.5px;
  }
  .brand__tagline {
    margin-top: 10px;
    color: var(--ink);
    font-size: 18px;
    line-height: 24px;
    letter-spacing: 0.6px;
  }

  .info-band {
    position: absolute;
    left: 0;
    top: 248px;
    width: 100%;
    height: 276px;
    background: var(--band-grey);
  }
  .info-band__rule {
    position: absolute;
    left: 0;
    width: 100%;
    height: 3px;
    background: var(--brand-blue);
  }
  .info-band__rule--top { top: 0; }
  .info-band__rule--bottom { top: 20px; }

  .info-band__divider {
    position: absolute;
    left: 438px;
    top: 48px;
    width: 2px;
    height: 181px;
    background: var(--brand-blue);
  }

  .advisor {
    position: absolute;
    left: 61px;
    top: 78px;
    color: var(--ink);
    font-size: 20px;
    line-height: 27px;
  }
  .advisor__name {
    color: var(--brand-blue);
    font-weight: 700;
    font-size: 27px;
    line-height: 34px;
    letter-spacing: 0.4px;
  }

  .contact {
    position: absolute;
    left: 518px;
    top: 70px;
    list-style: none;
    color: var(--ink);
    font-size: 20px;
    line-height: 28px;
  }
  .contact__item {
    display: flex;
    align-items: flex-start;
    margin-bottom: 3px;
  }
  .contact__icon {
    flex: none;
    width: 18px;
    height: 18px;
    margin: 5px 12px 0 0;
  }

  .disclosure {
    position: absolute;
    left: 80px;
    right: 80px;
    bottom: 44px;
    color: var(--muted-ink);
    font-size: 13px;
    line-height: 18px;
    text-align: center;
  }
</style>
</head>
<body>

<section class="card card--front" aria-label="Business card front">
  <div class="brand">
    <div class="brand__name">Harborlight Wealth Partners, LLC</div>
    <div class="brand__tagline">Turning Your Earned Income Into Retirement Income</div>
  </div>

  <div class="info-band">
    <div class="info-band__rule info-band__rule--top"></div>
    <div class="info-band__rule info-band__rule--bottom"></div>

    <div class="advisor">
      <div class="advisor__name">Neil Osgood, MBA</div>
      <div>ChFC®, CLU®</div>
      <div>Financial Advisor</div>
      <div>Registered Representative</div>
    </div>

    <div class="info-band__divider"></div>

    <ul class="contact">
      <li class="contact__item">
        <svg class="contact__icon" viewBox="0 0 18 18" aria-hidden="true">
          <rect width="18" height="18" fill="#2b55a0"/>
          <path d="M5 3.5h2.2l1 3-1.4 1.1a7 7 0 0 0 3.6 3.6l1.1-1.4 3 1v2.2c0 .6-.5 1-1 1A10.5 10.5 0 0 1 4 4.5c0-.5.4-1 1-1z" fill="#fff"/>
        </svg>
        <span>(555) 218-3960</span>
      </li>
      <li class="contact__item">
        <svg class="contact__icon" viewBox="0 0 18 18" aria-label="Fax">
          <rect width="18" height="18" fill="#2b55a0"/>
          <rect x="5.5" y="3" width="7" height="4" fill="none" stroke="#fff" stroke-width="1.2"/>
          <rect x="3" y="7" width="12" height="6" rx="1" fill="#fff"/>
          <rect x="5.5" y="11" width="7" height="4" fill="#2b55a0" stroke="#fff" stroke-width="1.2"/>
        </svg>
        <span>Fax: (555) 218-3961</span>
      </li>
      <li class="contact__item">
        <svg class="contact__icon" viewBox="0 0 18 18" aria-hidden="true">
          <rect width="18" height="18" fill="#2b55a0"/>
          <rect x="3.5" y="5" width="11" height="8" fill="none" stroke="#fff" stroke-width="1.3"/>
          <path d="M3.5 5 9 9.5 14.5 5" fill="none" stroke="#fff" stroke-width="1.3"/>
        </svg>
        <span>nosgood@harborlightwp.example</span>
      </li>
      <li class="contact__item">
        <svg class="contact__icon" viewBox="0 0 18 18" aria-hidden="true">
          <rect width="18" height="18" fill="#2b55a0"/>
          <path d="M9 3a4 4 0 0 1 4 4c0 3-4 8-4 8S5 10 5 7a4 4 0 0 1 4-4z" fill="#fff"/>
          <circle cx="9" cy="7" r="1.5" fill="#2b55a0"/>
        </svg>
        <span>2876 Meadowbrook Pkwy. Suite<br>K418 Virginia Beach, VA 23019</span>
      </li>
    </ul>
  </div>
</section>

<section class="card card--back" aria-label="Business card back">
  <div class="brand">
    <div class="brand__name">Harborlight Wealth Partners, LLC</div>
    <div class="brand__tagline">Turning Your Earned Income Into Retirement Income</div>
  </div>
  <p class="disclosure">Neil Osgood is a registered representative of and offers securities through Brightwater Capital Brokerage Corporation, Member SIPC. Brightwater Capital Brokerage Corporation is a member of the Brightwater Advisory Group which is the marketing name for Brightwater Holding Corporation and its affiliates.</p>
</section>

</body>
</html>
```